Fun but professional website required for school teaching consultancy.

Dear Designers,

I have an interesting brief for you. My client is a skilled teacher who is looking to promote her consultancy that provides bespoke training and support to other teachers.

She would like a website that promotes her philosophy for working with children, which is essentially that she wants to create a fun and creative learning environment for them, whilst maintaining the professionalism that is also required to succeed. Representation of the balance between these two points is crucial to the design.

Typically these kind of websites are pretty boring so we need something fun and vibrant, not uninviting ie those typical images of a teacher sat behind a desk or anything overly formal.

Here is an example of what we do not want: http://www.brightmarlowtutors.co.uk/ - in this one although my client liked the layout, she hated the graphics.

Here is a website that she really liked and captured the vibe of what she is trying to promote about herself: http://www.pennyvalekidsplace.com/ - this design indicates fun with learning, happy kids, lively colours and still has a professional feel as well.

If you have any further questions, please ask

Many thanks,

Gareth

PS Enclosed please find a whole bunch of resources (including site map) for this project. My client has supplied graphics, page content and plenty of visuals so hopefully this will make things easier
Updates

To all designers,

Thanks all your designs. Just to let you all know they have been sent to the client and I will supply feedback to you all individually when I get it.

Many thanks,
Gareth

Hi all,

We've had loads of designs for this project so thanks to you all very much. If there is any feedback to pass on, I will do this directly. Right now, all designs have been liked and are in the running. My client is going through them all and will make a decision on the deadline date which is the 10th May.
If you don't hear from me before then, it's simply because no alterations have been requested.

Many thanks.
Gareth

Industry/Entity Type

Training

```html
<!DOCTYPE html>
<html lang="en">
<head>
<meta charset="utf-8">
<title>Keystone Learning Consultancy Limited</title>
<link href="https://fonts.googleapis.com/css2?family=Open+Sans:wght@400;600;700&display=swap" rel="stylesheet">
<style>
:root{
  --blue:#0562b9;
  --blue-dark:#0b4f9c;
  --navy:#0f2d6e;
  --charcoal:#3b3b3b;
  --wine:#8c2a25;
  --orange:#d86a10;
  --text:#666;
  --ink:#222;
  --light:#f2f2f2;
  --footer:#2f2f2f;
}
*{box-sizing:border-box;margin:0;padding:0}
html,body{width:1150px;height:1200px;overflow:hidden;background:#fff;font-family:"Open Sans",sans-serif;color:var(--text)}
.canvas{position:relative;width:1150px;height:1200px}
.abs{position:absolute}
.header-band{left:0;top:0;width:1150px;height:158px;background:var(--blue)}
.brand{left:96px;top:0;width:109px;height:158px;background:#fff;padding:2px}
.brand-art{width:105px;height:115px;background:radial-gradient(circle at 50% 50%,#7fb6e6,#b9d8f1 70%)}
.brand-name{height:40px;background:#dde9f5;display:flex;align-items:center;justify-content:center;text-align:center;font-size:10px;font-weight:600;color:var(--blue-dark);line-height:15px}
.contact-top{right:129px;top:34px;text-align:right;color:#fff}
.contact-top .mail{font-size:14px}
.contact-top .call{font-size:21px;line-height:28px}
.mail-icon{left:1031px;top:41px}
.nav{left:252px;top:116px;height:42px;display:flex}
.nav a{display:flex;align-items:center;justify-content:center;height:42px;color:#fff;text-decoration:none;font-size:14px;font-weight:600;padding:0;white-space:nowrap;letter-spacing:-0.1px}
.nav .home{background:#fff;color:var(--blue);width:72px}
.nav .pe{background:var(--navy);width:105px}
.nav .courses{background:var(--charcoal);width:91px}
.nav .biopics{background:var(--wine);width:172px}
.nav .tl{background:var(--orange);width:125px}
.nav .resources{background:var(--charcoal);width:104px}
.nav .members{background:var(--navy);width:134px}
.hero-photo{left:95px;top:172px;width:718px;height:357px;background:linear-gradient(135deg,#4d5a2c,#8a9150 45%,#c9b89a 70%,#6b6a3a)}
.hero-panel{left:813px;top:172px;width:242px;height:357px;background:linear-gradient(180deg,#3a3a3a,#262626);padding:40px 20px 0 20px;color:#fff}
.hero-panel h2{font-size:19px;font-weight:400;line-height:26px}
.hero-panel p{font-size:13px;line-height:21px;color:#ccc;margin-top:8px}
.btn{display:inline-block;margin-top:14px;background:#fff;color:var(--blue);font-size:13px;padding:7px 12px;border-radius:2px}
.dots{left:885px;top:474px;width:97px;height:22px;border-radius:11px;background:#111;display:flex;align-items:center;justify-content:center;gap:10px}
.dots i{width:10px;height:10px;border-radius:50%;background:#fff;display:block}
.dots i.on{background:#111;border:2px solid #fff}
.arrow{top:477px}
.welcome{left:97px;top:550px;width:688px}
.welcome h1{font-size:22px;font-weight:700;color:var(--blue);line-height:30px;white-space:nowrap}
.welcome h3{font-size:16px;font-weight:400;color:var(--ink);margin-top:12px;line-height:22px}
.welcome p{font-size:13px;line-height:22px;margin-top:1px}
.welcome h3.second{margin-top:24px}
.blog{left:813px;top:546px;width:242px;height:396px;background:var(--light)}
.blog-head{height:40px;background:linear-gradient(180deg,#1767bd,#0b4a93);border-radius:4px 4px 0 0;color:#fff;font-size:18px;font-weight:700;padding:8px 16px}
.blog ul{list-style:none;padding:30px 14px 0 14px}
.blog li{display:flex;gap:14px;margin-bottom:26px}
.blog li svg{flex:none;margin-top:5px}
.blog a{color:var(--blue-dark);text-decoration:none;font-size:13px;line-height:20px;display:block}
.blog .date{font-size:13px;color:var(--ink);margin-top:6px}
.strip{left:0;top:972px;width:1150px;height:73px;background:var(--light)}
.info{font-size:13px;line-height:22px;color:var(--text);display:flex;align-items:center;gap:12px}
.tagline{left:0;top:1057px;width:1150px;text-align:center;font-size:24px;color:var(--blue)}
.footer{left:0;top:1102px;width:1150px;height:98px;background:var(--footer)}
.footer-links{left:97px;top:1124px;font-size:12.5px;color:#ccc}
.footer-links span{margin:0 7px}
.copyright{left:97px;top:1159px;font-size:12px;color:#ccc}
.social{left:930px;top:1138px;display:flex;gap:9px}
.social i{display:block;width:24px;height:24px;border-radius:50%;background:#777}
</style>
</head>
<body>
<div class="canvas">
  <div class="abs header-band"></div>
  <div class="abs brand">
    <div class="brand-art" role="img" aria-label="Blue painted handprints artwork"></div>
    <div class="brand-name">Keystone<br>Learning Ltd.</div>
  </div>
  <div class="abs contact-top">
    <div class="mail">Email: hello@keystonelearning.com</div>
    <div class="call">Call 07700 900418</div>
  </div>
  <svg class="abs mail-icon" width="24" height="30" viewBox="0 0 24 30"><rect x="1" y="1" width="20" height="28" fill="#fff"/><rect x="21" y="6" width="2" height="18" fill="#fff"/><text x="11" y="19" text-anchor="middle" font-size="12" fill="#0562b9" font-family="Open Sans,sans-serif">@</text></svg>
  <nav class="abs nav">
    <a class="home">HOME</a><a class="pe">PE SERVICES</a><a class="courses">COURSES</a><a class="biopics">CONSULTANT BIOPICS</a><a class="tl">T &amp; L SERVICES</a><a class="resources">RESOURCES</a><a class="members">MEMBERS ONLY</a>
  </nav>

  <div class="abs hero-photo" role="img" aria-label="Three children outdoors looking closely at a leaf"></div>
  <div class="abs hero-panel">
    <h2>Phasellus a metus pel lentesque</h2>
    <p>Aliquam nec rhoncus lacus. Pellentesque id imperdiet felis. Quisque ut nunc porttitor orci dignissim tempus. Morbi pulvinar diam nec sapien ultri-cies varius.</p>
    <span class="btn">Read more</span>
  </div>
  <svg class="abs arrow" style="left:842px" width="12" height="18" viewBox="0 0 12 18"><path d="M10 2 3 9l7 7" stroke="#fff" stroke-width="2" fill="none"/></svg>
  <div class="abs dots"><i class="on"></i><i></i><i></i><i></i></div>
  <svg class="abs arrow" style="left:1014px" width="12" height="18" viewBox="0 0 12 18"><path d="M2 2l7 7-7 7" stroke="#fff" stroke-width="2" fill="none"/></svg>

  <section class="abs welcome">
    <h1>WELCOME TO KEYSTONE LEARNING CONSULTANCY LIMITED</h1>
    <h3>What we Do</h3>
    <p>Keystone Learning specialises in providing bespoke Teaching and Learning and Physical Education support to the primary education sector.&nbsp; We offer a range of training and support methods, including team teaching, INSET, courses, coaching, mentoring, staff meetings and so on.&nbsp; Working with a diverse range of clients, such as individual primary and secondary schools, clusters,&nbsp; Hollybrook County Council, School Sports Partnerships, collaborations and Sports Coaches, we are committed to providing professional development that has a real impact on school improvement.Our consultants all bring with them a raft of experience in Primary Education, Physical Education and School Improvement, plus the skills to inspire and enthuse teachers.</p>
    <h3 class="second">Our Philosophy</h3>
    <p>We are passionate about teaching and learning – both ours and yours!&nbsp; We strive to practice what we preach and ensure that all our training and support is personalised for the group or individual that it is created for.&nbsp; We also know that our support is only as good as our own understanding, so we are dedicated to ensuring our own professional development and constantly reviewing and developing our practice.&nbsp; We work in partnership with our clients to design bespoke professional development opportunities, constantly reviewing and developing the support with the client to ensure their requirements are met.</p>
  </section>

  <aside class="abs blog">
    <div class="blog-head">LATEST BLOG</div>
    <ul>
      <li><svg width="12" height="12" viewBox="0 0 12 12"><path d="M2 2l4 4-4 4" stroke="#777" fill="none"/><path d="M10 1v10" stroke="#bbb"/></svg><div><a>Donec magna ante, congue ut nunc nec, aliquam elementum augue quis leo.</a><div class="date">April 29, 2014</div></div></li>
      <li><svg width="12" height="12" viewBox="0 0 12 12"><path d="M2 2l4 4-4 4" stroke="#777" fill="none"/><path d="M10 1v10" stroke="#bbb"/></svg><div><a>Donec magna ante, congue ut nunc nec, aliquam elementum augue quis leo.</a><div class="date">April 29, 2014</div></div></li>
      <li><svg width="12" height="12" viewBox="0 0 12 12"><path d="M2 2l4 4-4 4" stroke="#777" fill="none"/><path d="M10 1v10" stroke="#bbb"/></svg><div><a>Donec magna ante, congue ut nunc nec, aliquam elementum augue quis leo.</a><div class="date">April 29, 2014</div></div></li>
    </ul>
  </aside>

  <div class="abs strip"></div>
  <div class="abs info" style="left:128px;top:987px">
    <svg width="24" height="26" viewBox="0 0 24 26"><rect x="1" y="2" width="20" height="22" fill="none" stroke="#888" stroke-width="2"/><path d="M10 2v10l3-2 3 2V2" fill="#888"/></svg>
    <span>14 Orchard Lane, Hollybrook,<br>Kent. HB4 2QT</span>
  </div>
  <div class="abs info" style="left:436px;top:994px">
    <svg width="28" height="28" viewBox="0 0 28 28"><path d="M4 3c3-2 5 0 6 2l-2 3c2 5 6 9 11 11l3-2c2 1 4 3 2 6-3 3-8 2-13-3S1 6 4 3z" fill="#888" transform="rotate(15 14 14)"/></svg>
    <span>Phone: 07700 900418</span>
  </div>
  <div class="abs info" style="left:706px;top:996px">
    <svg width="27" height="20" viewBox="0 0 27 20"><rect x="0" y="0" width="27" height="20" fill="#888"/><path d="M1 1l12.5 10L26 1" stroke="#f2f2f2" stroke-width="2" fill="none"/></svg>
    <span>E-mail : hello@keystonelearning.co.uk</span>
  </div>

  <div class="abs tagline">A TEACHER EXPLAINS, A GREAT TEACHER INSPIRES</div>

  <footer class="abs footer"></footer>
  <div class="abs footer-links">Home<span>|</span>PE Services<span>|</span>Courses<span>|</span>Consultant Biopics<span>|</span>T &amp; L Services<span>|</span>Resources<span>|</span>Members Only</div>
  <div class="abs copyright">Copyright &nbsp;©&nbsp; 2014 &nbsp; Keystone Learning Consultancy Limited. &nbsp; All rights reserved.</div>
  <div class="abs social"><i></i><i></i><i></i><i></i></div>
</div>
</body>
</html>
```